IT Company needs full suite of stationery

Our company 4627 Vantrel Works Ltd. is an IT company based in Toronto, Canada. Based on our logo we would like to see business cards(front and back), letterhead, envelope, brochure template. Design would be simple, not too bright, modern but can be used for many years, good theme throughout. Our official logo is the the fullcolor_a, full company name is 4627 Vantrel Works Ltd., Please include full company name on all pieces. Logo can be modified to be the graphic only with the "4627 Works", I have cropped it myself for a couple files but I am no designer. We will provide lots of feedback so post early and often.
Updates

Project Deadline Extended
Reason: Very busy around the holidays, like a lot of the designs currently submitted, will definitely be picking one. Thanks for your submissions and merry Christmas and Happy New Year to everyone.

Industry/Entity Type

Business

```html
<!DOCTYPE html>
<html lang="en">
<head>
<meta charset="utf-8">
<title>4627 Vantrel Works Ltd. – Envelope</title>
<link href="https://fonts.googleapis.com/css2?family=Exo+2:wght@500;600&display=swap" rel="stylesheet">
<style>
  :root {
    --backdrop: #ececec;
    --paper: #f7f7f7;
    --paper-shade: #efefef;
    --edge: #dcdcdc;
    --brand-green: #3f9a2c;
    --brand-tint: #e3eedf;
    --ink: #3a3a3a;
    --ink-soft: #5a5a5a;
  }
  * { box-sizing: border-box; margin: 0; padding: 0; }
  html, body {
    width: 1200px; height: 795px; overflow: hidden;
    background: var(--backdrop);
    font-family: "Exo 2", Arial, sans-serif;
  }
  .canvas { position: relative; width: 1200px; height: 795px; }

  .envelope {
    position: absolute; top: 268px;
    width: 520px; height: 260px;
    background: var(--paper);
    border: 1px solid var(--edge);
    box-shadow: 0 6px 18px rgba(0,0,0,0.08);
    overflow: hidden;
  }
  .envelope--back { left: 50px; }
  .envelope--front { left: 630px; }

  .flap {
    position: absolute; left: 0; top: 0;
    width: 100%; height: 108px;
    background: var(--paper-shade);
    border-bottom: 1px solid var(--edge);
    border-radius: 0 0 14px 14px;
  }
  .flap-seal {
    position: absolute; left: 50%; top: 42px;
    transform: translateX(-50%);
    width: 26px; height: 26px; border-radius: 50%;
    background: var(--brand-green);
  }

  .watermark {
    position: absolute; right: -70px; top: 22px;
    width: 230px; height: 230px; border-radius: 50%;
    background: var(--brand-tint);
  }

  .brand {
    position: absolute; left: 30px; top: 30px;
    display: flex; align-items: center; gap: 10px;
  }
  .brand-dot {
    width: 34px; height: 34px; border-radius: 50%;
    background: var(--brand-green);
  }
  .brand-name {
    font-weight: 600; font-size: 22px; color: var(--ink);
    letter-spacing: 0.5px;
  }

  .address {
    position: absolute; left: 30px; bottom: 22px;
    font-size: 9px; line-height: 1.5; color: var(--ink-soft);
    font-weight: 500; font-style: normal;
  }
  .address-company { color: var(--ink); font-weight: 600; }
</style>
</head>
<body>
  <main class="canvas">
    <section class="envelope envelope--back" aria-label="Envelope back">
      <div class="flap">
        <span class="flap-seal"></span>
      </div>
    </section>

    <section class="envelope envelope--front" aria-label="Envelope front">
      <div class="watermark"></div>
      <div class="brand">
        <span class="brand-dot"></span>
        <span class="brand-name">4627 Works</span>
      </div>
      <address class="address">
        <span class="address-company">4627 Vantrel Works Ltd.</span><br>
        Harbourfront Lane 18 M5J 2N8<br>
        Toronto Canada
      </address>
    </section>
  </main>
</body>
</html>
```